R & T Summit Construction Business Card ideas

We want a business card to represents our company in a way that looks professional but is also a business card that is unique!

Industry/Entity Type

Construction Company

Contact Information for Business Card

open to all design ideas, just want to be able to see different options to choose from in either color or grayscale.

Requirements
Must have
• Our names and phone numbers
• Nolan Pritchett 512-804-2271
• Curtis Hale 512-693-1804
• Business logo

```html
<!DOCTYPE html>
<html lang="en">
<head>
<meta charset="utf-8">
<title>R &amp; T Summit Construction Business Card</title>
<link rel="stylesheet" href="https://fonts.googleapis.com/css2?family=Open+Sans:wght@400;600;700&display=swap">
<style>
  :root {
    --backdrop: #e9e7e4;
    --card: #ffffff;
    --ink: #111111;
    --text: #1c1c1c;
  }
  * { box-sizing: border-box; margin: 0; padding: 0; }
  html, body { width: 1200px; height: 1000px; overflow: hidden; }
  body {
    background: var(--backdrop);
    font-family: "Open Sans", Arial, sans-serif;
    color: var(--text);
    position: relative;
  }
  .business-card {
    position: absolute;
    left: 267px;
    width: 665px;
    height: 395px;
    background: var(--card);
    border-radius: 24px;
    overflow: hidden;
    box-shadow: 0 3px 10px rgba(0,0,0,0.18);
  }
  .business-card.front { top: 75px; }
  .business-card.back { top: 535px; }
  .contact-block {
    position: absolute;
    left: 32px;
    top: 58px;
  }
  .person-name {
    font-size: 19px;
    font-weight: 600;
    letter-spacing: 0.2px;
    line-height: 24px;
    text-transform: uppercase;
    color: var(--ink);
  }
  .contact-line {
    display: flex;
    align-items: center;
    gap: 5px;
    font-size: 16px;
    line-height: 22px;
    margin-bottom: 10px;
  }
  .contact-line svg { width: 13px; height: 13px; fill: var(--ink); flex: none; }
  .address {
    font-size: 15.5px;
    line-height: 23px;
    margin-top: 4px;
    margin-bottom: 16px;
  }
  .online .contact-line { margin-bottom: 2px; }
  .company-name {
    position: absolute;
    left: 338px;
    top: 148px;
    width: 300px;
    display: flex;
    align-items: center;
    gap: 10px;
    font-size: 25px;
    font-weight: 600;
    line-height: 30px;
    text-transform: uppercase;
    color: var(--ink);
  }
  .company-name .mark {
    width: 16px; height: 16px; background: var(--ink); flex: none;
  }
  .wave-band {
    position: absolute;
    left: 0; bottom: 0;
    width: 665px; height: 80px;
  }
</style>
</head>
<body>

<section class="business-card front">
  <div class="contact-block">
    <p class="person-name">Nolan Pritchett</p>
    <p class="contact-line"><svg viewBox="0 0 24 24"><path d="M6.6 10.8a15.1 15.1 0 0 0 6.6 6.6l2.2-2.2a1 1 0 0 1 1-.25 11.4 11.4 0 0 0 3.6.57 1 1 0 0 1 1 1V20a1 1 0 0 1-1 1A17 17 0 0 1 3 4a1 1 0 0 1 1-1h3.5a1 1 0 0 1 1 1c0 1.25.2 2.45.57 3.57a1 1 0 0 1-.25 1z"/></svg>512-804-2271</p>
    <p class="person-name">Curtis Hale</p>
    <p class="contact-line"><svg viewBox="0 0 24 24"><path d="M6.6 10.8a15.1 15.1 0 0 0 6.6 6.6l2.2-2.2a1 1 0 0 1 1-.25 11.4 11.4 0 0 0 3.6.57 1 1 0 0 1 1 1V20a1 1 0 0 1-1 1A17 17 0 0 1 3 4a1 1 0 0 1 1-1h3.5a1 1 0 0 1 1 1c0 1.25.2 2.45.57 3.57a1 1 0 0 1-.25 1z"/></svg>512-693-1804</p>
    <p class="address">4415 Ridgeline Ave 12 St,<br>Round Rock, TX 78664</p>
    <div class="online">
      <p class="contact-line"><svg viewBox="0 0 24 24"><path d="M2 5h20v14H2z M2 5l10 8 10-8" /></svg>info@rtsummitconstruction.com</p>
      <p class="contact-line"><svg viewBox="0 0 24 24"><circle cx="11" cy="11" r="9"/><path d="M14 14l8 4-3 1-1 3z" fill="#fff"/></svg>www.rtsummitconstruction.com</p>
    </div>
  </div>
  <p class="company-name"><span class="mark"></span>R &amp; T Summit Construction</p>
  <svg class="wave-band" viewBox="0 0 665 80" preserveAspectRatio="none" aria-hidden="true">
    <path d="M0 72 C120 20 240 0 360 12 C470 22 560 40 665 14 L665 80 L0 80 Z" fill="var(--ink)"/>
    <path d="M4 70 C140 36 260 26 380 36 C480 44 580 52 660 16" fill="none" stroke="#fff" stroke-width="3"/>
  </svg>
</section>

<section class="business-card back">
  <div class="contact-block">
    <p class="person-name">Nolan Pritchett</p>
    <p class="contact-line"><svg viewBox="0 0 24 24"><path d="M6.6 10.8a15.1 15.1 0 0 0 6.6 6.6l2.2-2.2a1 1 0 0 1 1-.25 11.4 11.4 0 0 0 3.6.57 1 1 0 0 1 1 1V20a1 1 0 0 1-1 1A17 17 0 0 1 3 4a1 1 0 0 1 1-1h3.5a1 1 0 0 1 1 1c0 1.25.2 2.45.57 3.57a1 1 0 0 1-.25 1z"/></svg>512-804-2271</p>
    <p class="person-name">Curtis Hale</p>
    <p class="contact-line"><svg viewBox="0 0 24 24"><path d="M6.6 10.8a15.1 15.1 0 0 0 6.6 6.6l2.2-2.2a1 1 0 0 1 1-.25 11.4 11.4 0 0 0 3.6.57 1 1 0 0 1 1 1V20a1 1 0 0 1-1 1A17 17 0 0 1 3 4a1 1 0 0 1 1-1h3.5a1 1 0 0 1 1 1c0 1.25.2 2.45.57 3.57a1 1 0 0 1-.25 1z"/></svg>512-693-1804</p>
    <p class="address">4415 Ridgeline Ave 12 St,<br>Round Rock, TX 78664</p>
    <div class="online">
      <p class="contact-line"><svg viewBox="0 0 24 24"><path d="M2 5h20v14H2z M2 5l10 8 10-8" /></svg>info@rtsummitconstruction.com</p>
      <p class="contact-line"><svg viewBox="0 0 24 24"><circle cx="11" cy="11" r="9"/><path d="M14 14l8 4-3 1-1 3z" fill="#fff"/></svg>www.rtsummitconstruction.com</p>
    </div>
  </div>
  <p class="company-name"><span class="mark"></span>R &amp; T Summit Construction</p>
  <svg class="wave-band" viewBox="0 0 665 80" preserveAspectRatio="none" aria-hidden="true">
    <path d="M0 72 C120 20 240 0 360 12 C470 22 560 40 665 14 L665 80 L0 80 Z" fill="var(--ink)"/>
    <path d="M4 70 C140 36 260 26 380 36 C480 44 580 52 660 16" fill="none" stroke="#fff" stroke-width="3"/>
  </svg>
</section>

</body>
</html>
```